Velmora Company

We sell our products into retail stores. We move our Kiosk into the store for a few days, the product sells through, and then we move on to the next store.
Our website is not a place to purchase product. It is only a place that will list the schedule of where/when our kiosk will be in retail stores, and also give the consumer a little more detail about us.
The more you can develop a site that adheres to the theme the better. Want it to be fun and fashionable. Animated ideas are fine, and welcome, but they would need to be coded in HTML5, not flash. So even though this is a design only project, if you are going to recommend some animations, please keep HTML5 in mind.
attached files have:
1. images of the display as seen in the store (without shawls). this is just so you see how we are presenting ourself at retail.
2. images of some of the graphics components that are in the retail display
3. the pdf of the actual words use in the retail display (color meanings). this is the concept that I think as a designer you could really run with. have fun with this one and see how you can thread it into a website.
4. a lot of custom illustrations we had made with the wraps that are in the show. these are part of our theme as well and so you can use these as part of your design. no need to overdo it, use them if it makes sense, or don't use them at all. its fine with us.
Target Market(s)
united states, east coast
Industry/Entity Type
Retail
Requirements
Must have
- 1. Home page that is fashionable, fun, and has a lot of color and play with the color meanings. There should only be 3 links from the home page (about us, contact us, schedules).
2. Secondary page where we will list the schedule for our retail shows. Secondary page should have a simple method for navigating to either the home page or the contact us, about us pages

```html
<!DOCTYPE html>
<html lang="en">
<head>
<meta charset="utf-8">
<title>Velmora Company</title>
<link rel="stylesheet" href="https://fonts.googleapis.com/css2?family=PT+Sans:wght@400;700&family=Ubuntu:wght@500;700&display=swap">
<style>
:root{
  --header-top:#e6dfec;
  --header-bottom:#b8a5cc;
  --nav:#4e2370;
  --nav-line:#6c3f8f;
  --pill:#8a48c6;
  --band:#8d6cab;
  --hero-bg:#efe3f1;
  --hero-dot:#e2cfe4;
  --deep:#4a1f6e;
  --ink:#2c2233;
  --accent:#b034d0;
  --meaning:#c21fc2;
  --muted:#8a8a8a;
  --card:#eeeeee;
  --line:#c9c9c9;
  --footer:#efecf2;
}
*{box-sizing:border-box;margin:0;padding:0}
html,body{width:1059px;height:1200px;overflow:hidden;background:#fff}
body{font-family:"PT Sans",Arial,sans-serif;color:var(--ink)}
a{color:inherit;text-decoration:none}
.canvas{position:relative;width:1059px;height:1200px;overflow:hidden;background:#fff}
.abs{position:absolute}

.site-header{left:0;top:0;width:1059px;height:87px;background:linear-gradient(90deg,#f1ecf4 0%,var(--header-top) 30%,var(--header-bottom) 100%)}
.brand{left:64px;top:18px;font-size:38px;font-weight:400;color:#1d1420;line-height:1}
.brand-tag{left:66px;top:60px;font-size:12.5px;color:#1d1420}
.search{left:803px;top:50px;width:190px;height:19px;background:#fff;border:1px solid #cfc6d8;font-size:11.5px;color:#8a8a8a;padding:2px 6px;line-height:14px}

.main-nav{left:0;top:87px;width:1059px;height:39px;background:var(--nav);border-top:1px solid #7a55a0;box-shadow:0 3px 4px rgba(40,10,60,.35)}
.nav-item{position:absolute;top:10px;font-size:14.5px;color:#fff;letter-spacing:.3px}
.nav-item.active{top:7px;left:62px;width:114px;height:24px;border-radius:12px;background:var(--pill);text-align:center;line-height:24px}
.nav-sep{position:absolute;top:2px;width:1px;height:34px;background:var(--nav-line)}

.hero-band{left:0;top:126px;width:1059px;height:441px;background:linear-gradient(90deg,#a48bbd,var(--band) 3%,#9d80b8 97%,#a48bbd)}
.hero{left:37px;top:128px;width:968px;height:435px;background:var(--hero-bg);overflow:hidden}
.hero-shadow{left:50px;top:570px;width:940px;height:14px;border-radius:50%;background:radial-gradient(ellipse at center,rgba(110,80,150,.45),rgba(110,80,150,0) 70%)}
.figure{position:absolute}
.headline{left:536px;top:268px;font-family:"Ubuntu",sans-serif;font-weight:700;font-size:34px;line-height:33px;color:var(--deep);letter-spacing:-.5px;white-space:nowrap}
.headline .hl{color:#6a3590}
.headline-box{display:inline-block;background:var(--deep);color:#fff;font-size:24px;padding:0 7px;line-height:31px;vertical-align:top;margin-left:4px}
.sub{left:538px;top:360px;font-size:15.5px;line-height:21px;color:#2c1f36;letter-spacing:.2px}
.sub .big{font-size:19px}
.lead{left:539px;top:404px;width:262px;font-size:13px;line-height:15px;color:#2c1f36}
.cta{left:539px;top:481px;width:104px;height:20px;background:var(--deep);color:#fff;font-size:12px;line-height:20px;padding-left:10px;letter-spacing:.4px;white-space:nowrap}
.arrow{top:317px;width:44px;height:43px;background:var(--deep)}
.arrow-left{left:32px;border-radius:0 8px 8px 0}
.arrow-right{left:967px;border-radius:8px 0 0 8px}

.panel-head{height:31px;background:var(--accent);color:#fff;font-size:17.5px;line-height:31px;padding-left:13px}
.categories{left:42px;top:606px;width:235px;height:465px;border:1px solid var(--line);border-top:none}
.categories .panel-head{margin:0 -1px}
.cat-list{list-style:none;padding:10px 0 0 14px}
.cat-list li{width:200px;height:26.2px;font-size:13px;color:var(--muted);line-height:19px;border-bottom:1px dotted #9a9a9a}

.whats-new{left:283px;top:606px;width:720px;height:527px;border:1px solid var(--line);border-top:none}
.whats-new .panel-head{margin:0 -1px}
.card{position:absolute;width:166px;height:208px;background:var(--card)}
.card-art{position:absolute;left:5px;top:5px;width:156px;height:152px;background:#fff}
.card-name{position:absolute;left:8px;top:166px;font-size:11.5px;color:#555}
.card-meta{position:absolute;left:8px;top:184px;font-size:10.5px;letter-spacing:.3px;white-space:nowrap}
.card-meta .tag{background:#fff;color:#999;padding:1px 5px;border:1px solid #e3e3e3}
.card-meta .meaning{color:var(--meaning);margin-left:4px}
.view-more{left:293px;top:1094px;width:85px;height:25px;border:1px solid #d6c4dc;border-radius:13px;background:#f6f0f7;color:var(--accent);font-size:13.5px;text-align:center;line-height:23px}

.site-footer{left:0;top:1133px;width:1059px;height:67px;background:var(--footer)}
.copyright{left:44px;top:11px;font-size:13.5px;color:#2a2a2a}
.footer-nav{right:61px;top:11px;font-size:13.5px;color:#2a2a2a}
.footer-nav span{margin:0 14px}
</style>
</head>
<body>
<div class="canvas">

  <header class="abs site-header">
    <div class="abs brand">Velmora</div>
    <div class="abs brand-tag">vel | mo | ra</div>
    <div class="abs search">search here</div>
  </header>

  <nav class="abs main-nav">
    <div class="nav-item active" aria-current="page">MAIN PAGE</div>
    <div class="nav-sep" style="left:207px"></div>
    <a class="nav-item" style="left:236px" href="#about">ABOUT US</a>
    <div class="nav-sep" style="left:341px"></div>
    <a class="nav-item" style="left:370px" href="#schedules">SCHEDULES</a>
    <div class="nav-sep" style="left:474px"></div>
    <a class="nav-item" style="left:503px" href="#contact">CONTACT US</a>
  </nav>

  <div class="abs hero-band"></div>
  <div class="abs hero-shadow"></div>
  <section class="abs hero">
    <svg class="figure" style="left:0;top:0" width="968" height="435" aria-hidden="true">
      <circle cx="500" cy="40" r="55" fill="var(--hero-dot)"/>
      <circle cx="600" cy="75" r="30" fill="var(--hero-dot)"/>
      <circle cx="840" cy="20" r="75" fill="var(--hero-dot)"/>
      <circle cx="250" cy="82" r="30" fill="var(--hero-dot)"/>
      <circle cx="660" cy="400" r="30" fill="var(--hero-dot)"/>
      <circle cx="100" cy="260" r="45" fill="var(--hero-dot)"/>
    </svg>
    <div class="figure" role="img" aria-label="Sketch of a woman wearing a long taupe shawl" style="left:61px;top:14px;width:176px;height:421px;background:linear-gradient(180deg,rgba(255,255,255,.55),rgba(140,128,118,.55) 40%,rgba(255,255,255,.4))"></div>
    <div class="figure" role="img" aria-label="Sketch of a woman wearing a plum shawl" style="left:242px;top:40px;width:236px;height:395px;background:linear-gradient(180deg,rgba(255,255,255,.6),rgba(135,72,105,.6) 45%,rgba(255,255,255,.5))"></div>
    <div class="figure" role="img" aria-label="Sketch of a woman wearing a red scarf" style="left:769px;top:84px;width:160px;height:351px;background:linear-gradient(180deg,rgba(255,255,255,.55),rgba(205,50,85,.45) 35%,rgba(180,180,180,.4))"></div>
  </section>

  <div class="abs headline">BEST <span class="hl">SHAWLS</span><br>IN<span class="headline-box">WHOLE MARKET</span></div>
  <div class="abs sub">THIS WINTER GETS<br><span class="big">SPECIAL OFFERS</span></div>
  <p class="abs lead">This definition separates web design from web programming, emphasizing the functional features of a web site, as well as positioning</p>
  <a class="abs cta" href="#schedules">SCHEDULES &nbsp;❯</a>

  <div class="abs arrow arrow-left">
    <svg width="44" height="43" aria-hidden="true"><circle cx="22" cy="21.5" r="12" fill="#fff" stroke="#c9bcd6" stroke-width="2"/><path d="M22 16l-5 5.5 5 5.5M27 16l-5 5.5 5 5.5" fill="none" stroke="#777" stroke-width="1.8"/></svg>
  </div>
  <div class="abs arrow arrow-right">
    <svg width="44" height="43" aria-hidden="true"><circle cx="22" cy="21.5" r="12" fill="#fff" stroke="#c9bcd6" stroke-width="2"/><path d="M17 16l5 5.5-5 5.5M22 16l5 5.5-5 5.5" fill="none" stroke="#777" stroke-width="1.8"/></svg>
  </div>

  <aside class="abs categories">
    <div class="panel-head">Categories</div>
    <ul class="cat-list">
      <li>Your First Section here</li>
      <li>Your Second Section here</li>
      <li>Your Thrid Section here</li>
      <li>Your More Category</li>
      <li>Your More Category</li>
      <li>Your More Category</li>
      <li>Your More Category</li>
      <li>Your More Category</li>
      <li>Your More Category</li>
      <li>Your More Category</li>
      <li>Your More Category</li>
      <li>Your More Category</li>
      <li>Your More Category</li>
      <li>Your More Category</li>
      <li>Your More Category</li>
    </ul>
  </aside>

  <section class="abs whats-new">
    <div class="panel-head">What’s New</div>

    <div class="card" style="left:10px;top:37px"><div class="card-art" role="img" aria-label="Sketch of a woman in a blue shawl" style="background:linear-gradient(180deg,#fff 25%,#7a74e0 60%,#fff)"></div><div class="card-name">Name of Shawl</div><div class="card-meta"><span class="tag">Blue shade</span><span class="meaning">Calm &amp; trust</span></div></div>
    <div class="card" style="left:185px;top:37px"><div class="card-art" role="img" aria-label="Sketch of a woman in a grey scarf" style="background:linear-gradient(180deg,#fff 25%,#9aa39d 60%,#fff)"></div><div class="card-name">Name of Shawl</div><div class="card-meta"><span class="tag">Grey shade</span><span class="meaning">Balance</span></div></div>
    <div class="card" style="left:362px;top:37px"><div class="card-art" role="img" aria-label="Sketch of a woman in a plum scarf" style="background:linear-gradient(180deg,#fff 25%,#a56680 60%,#fff)"></div><div class="card-name">Name of Shawl</div><div class="card-meta"><span class="tag">Plum shade</span><span class="meaning">Luxury</span></div></div>
    <div class="card" style="left:537px;top:37px"><div class="card-art" role="img" aria-label="Sketch of a woman in a cream shawl" style="background:linear-gradient(180deg,#fff 25%,#e2dcd4 60%,#fff)"></div><div class="card-name">Name of Shawl</div><div class="card-meta"><span class="tag">Cream shade</span><span class="meaning">Purity</span></div></div>

    <div class="card" style="left:12px;top:258px"><div class="card-art" role="img" aria-label="Sketch of a woman in an orange scarf" style="background:linear-gradient(180deg,#fff 25%,#e3936b 60%,#fff)"></div><div class="card-name">Name of Shawl</div><div class="card-meta"><span class="tag">Rust shade</span><span class="meaning">Warmth</span></div></div>
    <div class="card" style="left:187px;top:258px"><div class="card-art" role="img" aria-label="Sketch of a woman in a turquoise scarf" style="background:linear-gradient(180deg,#fff 20%,#5cc0e8 60%,#fff)"></div><div class="card-name">Name of Shawl</div><div class="card-meta"><span class="tag">Aqua shade</span><span class="meaning">Freshness</span></div></div>
    <div class="card" style="left:364px;top:258px"><div class="card-art" role="img" aria-label="Sketch of a woman in a green scarf" style="background:linear-gradient(180deg,#fff 25%,#4f8a5c 60%,#fff)"></div><div class="card-name">Name of Shawl</div><div class="card-meta"><span class="tag">Green shade</span><span class="meaning">Growth</span></div></div>
    <div class="card" style="left:539px;top:258px"><div class="card-art" role="img" aria-label="Sketch of a woman in a red scarf" style="background:linear-gradient(180deg,#fff 25%,#cf5470 60%,#fff)"></div><div class="card-name">Name of Shawl</div><div class="card-meta"><span class="tag">Red shade</span><span class="meaning">Passion</span></div></div>
  </section>

  <div class="abs view-more">view more</div>

  <footer class="abs site-footer">
    <div class="abs copyright">copyright © 2011 Velmora company All right reserved</div>
    <nav class="abs footer-nav"><a href="#about">About us</a><span>|</span><a href="#schedules">Schedules</a><span>|</span><a href="#contact">Contact us</a></nav>
  </footer>

</div>
</body>
</html>
```